Harborline Outpost Atlas needs a web design

We are launching a new website and need a web design. The website is going to list every military base and installment around the world with information on each base such as a description of the base, the history of the base, contact information at the base, address, lat/long of the base, and any other relevant information including images of the base. We need a home page with navigation menu and the design of the military base page so that every military base page is formatted the same for the referenced information. We have included an example of the content that may be found on the base page(s). We are also going to have the information available in spanish.

We also wanted to mention we will be building this website in wordpress.

We also wanted to note that in the format of each base page, we will have a frequently asked questions section with answers.

```html
<!DOCTYPE html>
<html lang="en">
<head>
<meta charset="utf-8">
<title>Harborline Outpost Atlas</title>
<link href="https://fonts.googleapis.com/css2?family=Montserrat:wght@400;500;600;700;800&family=Playfair+Display:wght@700;800&display=swap" rel="stylesheet">
<style>
:root{
  --red:#b0131c;
  --green:#0c5a2b;
  --ink:#2a2a2a;
  --muted:#666;
  --light:#f2f2f2;
  --line:#e2e2e2;
  --black:#111;
  --white:#fff;
}
*{margin:0;padding:0;box-sizing:border-box}
html,body{width:1200px;height:3008px;overflow:hidden}
body{font-family:"Montserrat",sans-serif;color:var(--ink);background:var(--white);position:relative}
.brand{font-family:"Playfair Display",serif;font-weight:800;font-size:26px;color:var(--black)}
.nav{display:flex;gap:6px;align-items:center}
.nav a{font-size:12px;font-weight:600;color:var(--ink);text-decoration:none;padding:8px 10px;letter-spacing:.3px}
.nav a.active{background:var(--red);color:var(--white)}

.site-header{height:76px;display:flex;align-items:center;justify-content:space-between;padding:0 92px 0 120px}

.hero{height:516px;position:relative;background:linear-gradient(180deg,#5e6a70 0%,#7b8378 45%,#8c8467 75%,#6f6a58 100%);text-align:center;color:var(--white)}
.hero::after{content:"";position:absolute;inset:0;background:rgba(0,0,0,.25)}
.hero-inner{position:relative;z-index:1;padding-top:130px}
.hero h1{font-size:36px;font-weight:800;letter-spacing:.5px}
.hero p{font-size:15px;font-weight:500;width:620px;margin:12px auto 0;line-height:1.5}
.search{width:560px;height:52px;margin:50px auto 0;background:var(--white);border-radius:26px;display:flex;align-items:center;justify-content:space-between;padding:0 6px 0 28px}
.search span{font-size:12px;font-weight:600;color:#444}
.search-btn{width:42px;height:42px;border-radius:50%;background:var(--green);display:flex;align-items:center;justify-content:center}

.section-title{text-align:center;font-size:22px;font-weight:800;color:var(--black);letter-spacing:.3px}
.section-title::after{content:"";display:block;width:50px;height:3px;background:var(--green);margin:10px auto 0}

.bases{height:440px;padding-top:32px}
.base-grid{display:grid;grid-template-columns:repeat(4,225px);gap:10px;justify-content:center;margin-top:36px}
.photo{display:block}
.base-card .photo{height:162px}
.card-title{font-size:11.5px;font-weight:700;color:var(--green);line-height:1.35;margin-top:12px}
.card-meta{font-size:11px;color:var(--muted);line-height:1.55;margin-top:6px}

.featured{height:705px;background:var(--light);padding:50px 120px 0}
.featured-head{display:flex;justify-content:space-between;align-items:center}
.featured-head h2{font-size:22px;font-weight:800;color:var(--black)}
.featured-head h2::after{content:"";display:block;width:50px;height:3px;background:var(--green);margin-top:10px}
.btn-green{background:var(--green);color:var(--white);font-size:11px;font-weight:700;padding:11px 20px;border-radius:3px}
.featured-grid{display:grid;grid-template-columns:repeat(2,468px);gap:22px 24px;margin-top:28px}
.listing{background:var(--white);height:176px;display:flex;padding:14px;gap:18px;box-shadow:0 2px 6px rgba(0,0,0,.06)}
.listing .photo{width:150px;height:148px;flex:none}
.listing .card-title{margin-top:4px;font-size:12px}
.btn-red{display:inline-block;background:var(--red);color:var(--white);font-size:9.5px;font-weight:700;padding:7px 12px;border-radius:2px;margin-top:14px}

.reviews{height:500px;padding-top:70px;position:relative}
.review-grid{display:grid;grid-template-columns:repeat(3,290px);gap:30px;justify-content:center;margin-top:40px}
.review{background:var(--white);box-shadow:0 3px 14px rgba(0,0,0,.12);padding:26px 24px;height:262px}
.quote-row{display:flex;align-items:center;gap:10px}
.quote{font-family:"Playfair Display",serif;font-size:46px;color:var(--red);line-height:.6;height:24px}
.review p{font-size:12px;line-height:1.6;color:#444;margin-top:12px}
.reviewer{font-size:12px;font-weight:700;color:var(--green);margin-top:16px}
.arrow{position:absolute;top:292px}
.arrow.left{left:72px}.arrow.right{right:72px}

.blog{height:627px;background:var(--light);padding-top:48px}
.blog-grid{display:grid;grid-template-columns:repeat(3,300px);gap:30px;justify-content:center;margin-top:40px}
.post{background:var(--white);height:460px}
.post .photo{height:206px}
.post-body{padding:20px 22px}
.post h3{font-size:19px;font-weight:700;color:var(--green);line-height:1.3}
.post p{font-size:11px;line-height:1.6;color:var(--muted);margin-top:10px}

.site-footer{height:160px;background:var(--black);color:var(--white);padding:0 120px}
.footer-top{height:100px;display:flex;justify-content:space-between;align-items:center;border-bottom:1px solid #333}
.site-footer .brand{color:var(--white)}
.site-footer .nav a{color:var(--white);font-weight:500}
.copyright{text-align:center;font-size:11px;color:#bbb;padding-top:20px}
</style>
</head>
<body>

<header class="site-header">
  <div class="brand">Harborline Outpost Atlas</div>
  <nav class="nav">
    <a class="active">HOME</a><a>ABOUT US</a><a>SERVICES</a><a>BASE DIRECTORY</a><a>BLOG</a><a>CONTACT US</a>
  </nav>
</header>

<section class="hero" role="img" aria-label="Aerial photograph of a military base with rows of vehicles and buildings">
  <div class="hero-inner">
    <h1>HARBORLINE OUTPOST ATLAS</h1>
    <p>Lorem ipsum dolor sit amet, consectetur adipiscing elit, sed do eiusmod tempor incididunt ut labore et dolore magna.</p>
    <div class="search">
      <span>SEARCH FOR A BASE</span>
      <div class="search-btn">
        <svg width="18" height="18" viewBox="0 0 24 24" fill="none" stroke="#fff" stroke-width="3"><circle cx="10" cy="10" r="7"/><line x1="15.5" y1="15.5" x2="21" y2="21"/></svg>
      </div>
    </div>
  </div>
</section>

<section class="bases">
  <h2 class="section-title">MILITARY BASE</h2>
  <div class="base-grid">
    <article class="base-card">
      <div class="photo" role="img" aria-label="Desert base with mountains and aircraft" style="background:linear-gradient(180deg,#8ea3b8,#b59a78 60%,#8a7558)"></div>
      <h3 class="card-title">Fort Alder Military Base History, Facilities, and Support Services</h3>
      <p class="card-meta">Alder Ridge, KY United States<br>Number: (555) 014-2270</p>
    </article>
    <article class="base-card">
      <div class="photo" role="img" aria-label="Soldiers and vehicles on base grounds" style="background:linear-gradient(180deg,#a9a79c,#76705d 60%,#5a5444)"></div>
      <h3 class="card-title">Fort Alder Military Base History, Facilities, and Support Services</h3>
      <p class="card-meta">Alder Ridge, KY United States<br>Number: (555) 014-2270</p>
    </article>
    <article class="base-card">
      <div class="photo" role="img" aria-label="Aerial view of base barracks" style="background:linear-gradient(180deg,#7f8f74,#a69a7d 55%,#6f6a55)"></div>
      <h3 class="card-title">Fort Alder Military Base History, Facilities, and Support Services</h3>
      <p class="card-meta">Alder Ridge, KY United States<br>Number: (555) 014-2270</p>
    </article>
    <article class="base-card">
      <div class="photo" role="img" aria-label="Aerial view of base buildings and roads" style="background:linear-gradient(180deg,#8c8a70,#b1a583 55%,#7d7659)"></div>
      <h3 class="card-title">Fort Alder Military Base History, Facilities, and Support Services</h3>
      <p class="card-meta">Alder Ridge, KY United States<br>Number: (555) 014-2270</p>
    </article>
  </div>
</section>

<section class="featured">
  <div class="featured-head">
    <h2>FEATURED BASE LISTINGS</h2>
    <span class="btn-green">VIEW ALL LISTINGS</span>
  </div>
  <div class="featured-grid">
    <article class="listing">
      <div class="photo" role="img" aria-label="Base airfield with aircraft" style="background:linear-gradient(160deg,#9aa4a8,#7c7865)"></div>
      <div><h3 class="card-title">Fort Alder Military Base History, Facilities, and Support Services</h3><p class="card-meta">Alder Ridge, KY United States<br>Number: (555) 014-2270</p><span class="btn-red">READ MORE</span></div>
    </article>
    <article class="listing">
      <div class="photo" role="img" aria-label="Aerial view of base compound" style="background:linear-gradient(160deg,#7e8a6e,#a49b7f)"></div>
      <div><h3 class="card-title">Fort Alder Military Base History, Facilities, and Support Services</h3><p class="card-meta">Alder Ridge, KY United States<br>Number: (555) 014-2270</p><span class="btn-red">READ MORE</span></div>
    </article>
    <article class="listing">
      <div class="photo" role="img" aria-label="Base buildings surrounded by trees" style="background:linear-gradient(160deg,#6f7f5c,#8f8a6e)"></div>
      <div><h3 class="card-title">Fort Alder Military Base History, Facilities, and Support Services</h3><p class="card-meta">Alder Ridge, KY United States<br>Number: (555) 014-2270</p><span class="btn-red">READ MORE</span></div>
    </article>
    <article class="listing">
      <div class="photo" role="img" aria-label="Aircraft parked on base tarmac" style="background:linear-gradient(160deg,#8d9486,#6d7462)"></div>
      <div><h3 class="card-title">Fort Alder Military Base History, Facilities, and Support Services</h3><p class="card-meta">Alder Ridge, KY United States<br>Number: (555) 014-2270</p><span class="btn-red">READ MORE</span></div>
    </article>
    <article class="listing">
      <div class="photo" role="img" aria-label="Aerial view of base grounds and fields" style="background:linear-gradient(160deg,#a0966f,#6f7a58)"></div>
      <div><h3 class="card-title">Fort Alder Military Base History, Facilities, and Support Services</h3><p class="card-meta">Alder Ridge, KY United States<br>Number: (555) 014-2270</p><span class="btn-red">READ MORE</span></div>
    </article>
    <article class="listing">
      <div class="photo" role="img" aria-label="Base hangars under blue sky" style="background:linear-gradient(180deg,#9fb2c4,#6e7456)"></div>
      <div><h3 class="card-title">Fort Alder Military Base History, Facilities, and Support Services</h3><p class="card-meta">Alder Ridge, KY United States<br>Number: (555) 014-2270</p><span class="btn-red">READ MORE</span></div>
    </article>
  </div>
</section>

<section class="reviews">
  <h2 class="section-title">REVIEWS</h2>
  <svg class="arrow left" width="14" height="22" viewBox="0 0 14 22"><polyline points="11,2 3,11 11,20" fill="none" stroke="#222" stroke-width="3"/></svg>
  <svg class="arrow right" width="14" height="22" viewBox="0 0 14 22"><polyline points="3,2 11,11 3,20" fill="none" stroke="#222" stroke-width="3"/></svg>
  <div class="review-grid">
    <article class="review">
      <div class="quote-row"><span class="quote">&ldquo;</span><svg width="80" height="14" viewBox="0 0 80 14" fill="#b0131c"><g id="star"><polygon points="7,0 8.8,5 14,5 9.8,8.2 11.4,13.5 7,10.3 2.6,13.5 4.2,8.2 0,5 5.2,5"/></g><use href="#star" x="16"/><use href="#star" x="32"/><use href="#star" x="48"/><use href="#star" x="64"/></svg></div>
      <p>Sed ut perspiciatis unde omnis iste natus error sit voluptatem accusantium doloremque laudantium, totam rem aperiam, eaque ipsa quae ab illo inventore veritatis et quasi architecto beatae vitae dicta sunt explicabo.</p>
      <div class="reviewer">RICHARD</div>
    </article>
    <article class="review">
      <div class="quote-row"><span class="quote">&ldquo;</span><svg width="80" height="14" viewBox="0 0 80 14" fill="#b0131c"><use href="#star"/><use href="#star" x="16"/><use href="#star" x="32"/><use href="#star" x="48"/><use href="#star" x="64"/></svg></div>
      <p>Sed ut perspiciatis unde omnis iste natus error sit voluptatem accusantium doloremque laudantium, totam rem aperiam, eaque ipsa quae ab illo inventore veritatis et quasi architecto beatae vitae dicta sunt explicabo.</p>
      <div class="reviewer">RICHARD</div>
    </article>
    <article class="review">
      <div class="quote-row"><span class="quote">&ldquo;</span><svg width="80" height="14" viewBox="0 0 80 14" fill="#b0131c"><use href="#star"/><use href="#star" x="16"/><use href="#star" x="32"/><use href="#star" x="48"/><use href="#star" x="64"/></svg></div>
      <p>Sed ut perspiciatis unde omnis iste natus error sit voluptatem accusantium doloremque laudantium, totam rem aperiam, eaque ipsa quae ab illo inventore veritatis et quasi architecto beatae vitae dicta sunt explicabo.</p>
      <div class="reviewer">RICHARD</div>
    </article>
  </div>
</section>

<section class="blog">
  <h2 class="section-title">LATEST BLOG</h2>
  <div class="blog-grid">
    <article class="post">
      <div class="photo" role="img" aria-label="Base building lit at dusk" style="background:linear-gradient(180deg,#3e4a5c,#8b7a5a 70%,#5b5040)"></div>
      <div class="post-body"><h3>Sed ut perspiciatis unde omnis iste natus error sit voluptatem</h3><p>Ut enim ad minima veniam, quis nostrum exercitationem ullam corporis suscipit laboriosam, nisi ut aliquid ex ea commodi consequatur.</p><span class="btn-red">READ MORE</span></div>
    </article>
    <article class="post">
      <div class="photo" role="img" aria-label="Aircraft displayed on base field" style="background:linear-gradient(180deg,#a9b8c6,#7f8b6a 60%,#5f6a4c)"></div>
      <div class="post-body"><h3>Sed ut perspiciatis unde omnis iste natus error sit voluptatem</h3><p>Ut enim ad minima veniam, quis nostrum exercitationem ullam corporis suscipit laboriosam, nisi ut aliquid ex ea commodi consequatur.</p><span class="btn-red">READ MORE</span></div>
    </article>
    <article class="post">
      <div class="photo" role="img" aria-label="Aerial view of base in dry landscape" style="background:linear-gradient(180deg,#9c9072,#b4a47f 55%,#7d6d50)"></div>
      <div class="post-body"><h3>Sed ut perspiciatis unde omnis iste natus error sit voluptatem</h3><p>Ut enim ad minima veniam, quis nostrum exercitationem ullam corporis suscipit laboriosam, nisi ut aliquid ex ea commodi consequatur.</p><span class="btn-red">READ MORE</span></div>
    </article>
  </div>
</section>

<footer class="site-footer">
  <div class="footer-top">
    <div class="brand">Harborline Outpost Atlas</div>
    <nav class="nav"><a>HOME</a><a>ABOUT US</a><a>SERVICES</a><a>BASE DIRECTORY</a><a>BLOG</a><a>CONTACT US</a></nav>
  </div>
  <p class="copyright">Copyright © 2023 All Rights Reserved</p>
</footer>

</body>
</html>
```